Business Card Design Project

We require business cards to be produced with the following design
http://files.pixelvault-demo.net/img/50329/84172/84172_2093548_50329_image.jpg
Rather than bright meadow, please use Vantelo as the comapny name.
Please also use the following contact details:
1.
Daniel Overbeck
Entrepreneur
07423158871
doverbeck@vantelo-demo.com
2.
Tom Ashworth
Founder
07539402217
tashworth@vantelo-demo.com
Please add:
Facebook favicion pagehub.com/vantelo
Linked in favicon proflink/danieloverbeck
Skype favicon doverbeck
Linked in favicon linkedin/thomasashworth
Skype favicon thomasashworth
Google Plus favicon tomashworth@mailbox-demo.net
To the back

```html
<!DOCTYPE html>
<html lang="en">
<head>
<meta charset="utf-8">
<title>Vantelo Business Cards</title>
<link rel="stylesheet" href="https://fonts.googleapis.com/css2?family=Russo+One&family=Arimo:wght@400&display=swap">
<style>
  :root {
    --stage: #2b2b2b;
    --brand-red: #e31e26;
    --card-white: #f4f4f4;
    --panel-grey: #e9e9e9;
    --text-grey: #6d6d6d;
    --logo-grey: #7a7a7a;
    --divider: #b9b9b9;
    --white: #ffffff;
  }
  html, body {
    margin: 0;
    width: 1200px;
    height: 900px;
    overflow: hidden;
    background: var(--stage);
  }
  .canvas {
    position: relative;
    width: 1200px;
    height: 900px;
  }
  .card {
    position: absolute;
    width: 560px;
    height: 320px;
    border-radius: 2px;
    box-shadow: 0 18px 40px rgba(0,0,0,0.45);
    overflow: hidden;
  }

  /* Back of card */
  .card-back {
    left: 150px;
    top: 110px;
    background: var(--brand-red);
  }
  .card-back .brand-square {
    position: absolute;
    left: 40px;
    top: 96px;
    width: 190px;
    height: 190px;
    border-radius: 34px;
    background: var(--white);
  }
  .card-back .brand-name {
    position: absolute;
    left: 262px;
    top: 30px;
    margin: 0;
    font-family: "Russo One", sans-serif;
    font-size: 50px;
    font-weight: 400;
    letter-spacing: 1px;
    color: var(--white);
  }
  .social-list {
    position: absolute;
    left: 268px;
    top: 104px;
    margin: 0;
    padding: 0;
    list-style: none;
    font-family: "Arimo", sans-serif;
    font-size: 16px;
    line-height: 24px;
    color: var(--white);
  }
  .social-list li {
    display: flex;
    align-items: center;
    gap: 7px;
  }
  .social-list .icon-box {
    width: 12px;
    height: 12px;
    border-radius: 2px;
    background: var(--white);
  }

  /* Front of card */
  .card-front {
    left: 490px;
    top: 440px;
    background: var(--card-white);
  }
  .logo-panel {
    position: absolute;
    left: 36px;
    top: 46px;
    width: 230px;
    height: 230px;
    border-radius: 40px;
    background: var(--panel-grey);
  }
  .logo-panel .brand-square {
    position: absolute;
    left: 62px;
    top: 30px;
    width: 106px;
    height: 106px;
    border-radius: 20px;
    background: var(--brand-red);
  }
  .logo-panel .brand-name {
    position: absolute;
    left: 0;
    right: 0;
    top: 152px;
    margin: 0;
    text-align: center;
    font-family: "Russo One", sans-serif;
    font-size: 36px;
    font-weight: 400;
    color: var(--logo-grey);
  }
  .divider {
    position: absolute;
    left: 290px;
    top: 92px;
    width: 1px;
    height: 130px;
    background: var(--divider);
  }
  .contact {
    position: absolute;
    left: 308px;
    top: 84px;
    font-family: "Arimo", sans-serif;
    color: var(--text-grey);
  }
  .contact .person-name {
    margin: 0;
    font-family: "Russo One", sans-serif;
    font-size: 23px;
    font-weight: 400;
    color: var(--brand-red);
  }
  .contact .role {
    margin: 2px 0 16px;
    font-size: 15px;
  }
  .contact .detail {
    margin: 0;
    font-size: 16px;
    line-height: 23px;
  }
</style>
</head>
<body>
<main class="canvas">
  <section class="card card-back" aria-label="Card back">
    <div class="brand-square"></div>
    <h2 class="brand-name">VANTELO</h2>
    <ul class="social-list">
      <li><span class="icon-box"></span>pagehub.com/vantelo</li>
      <li><span class="icon-box"></span>proflink/danieloverbeck</li>
      <li><span class="icon-box"></span>doverbeck</li>
    </ul>
  </section>

  <section class="card card-front" aria-label="Card front">
    <div class="logo-panel">
      <div class="brand-square"></div>
      <h2 class="brand-name">VANTELO</h2>
    </div>
    <div class="divider"></div>
    <div class="contact">
      <h1 class="person-name">Daniel Overbeck</h1>
      <p class="role">Entrepreneur</p>
      <p class="detail">07423158871</p>
      <p class="detail">doverbeck@vantelo-demo.com</p>
    </div>
  </section>
</main>
</body>
</html>
```